Flyer Handout when attending Dental Conventions, or dental office shows

take the sample file folder that is shown with 2 pictures. The outside and inside of the folder needs to be completed, along with the inserts. This folder pictures are from someone elses flyer/folder and i would like to have it layout like this. The KPW inserts is informational, but it is lacking originality, pictures, etc. Try to make our information and move it to 2017. When this is done, i would like to take this flyer and load it to the web or allow to send via email and make it interactive. The user can select the flyers and it will slide or flip to the flyer. this will make if kewl/fun

Target Market(s)

Dental Offices

Industry/Entity Type

Dental

Font styles to use
Serif
Sans Serif

Colors

Designer to choose colors to be used in the design.

Requirements
Must have
• a Semi new look and feel of our flyers, and a new envelope created

```html
<!DOCTYPE html>
<html lang="en">
<head>
<meta charset="utf-8">
<title>KPW Folder</title>
<link href="https://fonts.googleapis.com/css2?family=Montserrat:wght@400;500;600;700;800&family=PT+Serif:wght@700&display=swap" rel="stylesheet">
<style>
:root{
  --blue:#0b57a4;
  --blue-dark:#083f7c;
  --orange:#e8590f;
  --orange-light:#f07a2e;
  --ink:#2a2a2a;
  --paper:#ffffff;
  --bg:#e9e9ea;
  --ghost:#ececec;
}
*{box-sizing:border-box;margin:0;padding:0}
html,body{width:1096px;height:1200px;overflow:hidden;background:var(--bg);font-family:'Montserrat',sans-serif;color:var(--ink)}
.spread{position:absolute;left:128px;width:840px;height:560px;display:flex;box-shadow:0 10px 30px rgba(0,0,0,.18)}
.spread.outside{top:30px}
.spread.inside{top:620px}
.page{position:relative;width:420px;height:560px;background:var(--paper);overflow:hidden}
.top-bars{position:absolute;top:14px;left:0;right:0;height:6px}
.top-bars .bar{position:absolute;top:0;height:6px}
.bar.orange{background:var(--orange)}
.bar.blue{background:var(--blue)}
.brand{font-weight:800;color:var(--blue);letter-spacing:1px;display:flex;align-items:center;gap:6px}
.brand .dot{width:10px;height:10px;border-radius:50%;background:var(--orange)}
.ghost-mark{position:absolute;font-family:'Montserrat',sans-serif;font-weight:800;color:var(--ghost);line-height:1}
/* back cover */
.back .ghost-mark{font-size:170px;left:-30px;top:170px;transform:rotate(-90deg)}
.back .brand{position:absolute;left:28px;top:420px;font-size:34px}
.hours{position:absolute;left:28px;top:470px;font-size:11px;line-height:1.4}
.hours .label{color:var(--orange)}
.hours .label b{color:var(--blue)}
.hours .days{color:var(--orange);font-weight:700;font-size:12px}
.hours .time{color:var(--blue);font-weight:700;font-size:12px}
.divider{position:absolute;left:205px;top:410px;width:2px;height:100px;background:var(--orange)}
.contact-mini{position:absolute;left:222px;top:396px;font-size:9.5px;line-height:1.55;color:var(--blue-dark)}
.contact-mini h4{font-size:11px;color:var(--blue-dark)}
.contact-mini h4 span{color:var(--orange)}
.contact-mini .co{font-weight:700;font-size:11px;margin-bottom:4px}
.contact-mini .co span{color:var(--orange)}
.row{display:flex;align-items:center;gap:6px}
.row svg{width:9px;height:9px;flex:none}
.bottom-band{position:absolute;left:0;bottom:0;width:420px;height:34px}
/* front cover */
.front .hero{position:absolute;left:0;top:0}
.front .brand{position:absolute;left:40px;top:345px;font-size:34px}
.welcome{position:absolute;left:40px;top:395px;border-left:2px solid var(--orange);padding-left:12px}
.welcome .small{font-size:21px;color:var(--blue-dark);font-weight:500}
.welcome .big{font-size:23px;font-weight:800;color:var(--orange);line-height:1.2}
.web-pill{position:absolute;right:0;top:448px;background:var(--orange);color:#fff;font-size:9.5px;padding:4px 14px;border-radius:10px 0 0 10px;display:flex;gap:5px;align-items:center}
/* inside left */
.inside-left .brand{position:absolute;right:28px;top:34px;font-size:22px}
.intro{position:absolute;left:24px;top:70px;width:372px}
.intro .small{font-size:11px;color:var(--orange);font-weight:500}
.intro h2{font-size:13px;color:var(--blue-dark);font-weight:700;margin-bottom:6px}
.intro p{font-size:7.4px;line-height:1.45;margin-bottom:6px;text-align:justify}
.services-title{position:absolute;left:150px;top:250px;background:var(--blue);color:#fff;font-size:12px;font-weight:700;padding:3px 16px;border-radius:12px}
.services{position:absolute;left:24px;top:274px;width:372px}
.group-head{background:var(--blue);color:#fff;font-weight:700;font-size:10px;text-align:center;padding:2px 0}
.group-head.orange{background:var(--orange)}
.tags{display:grid;grid-template-columns:repeat(4,1fr);gap:3px;margin:3px 0 5px}
.tag{font-size:7px;font-weight:600;color:#fff;text-align:center;padding:3px 2px;font-style:normal}
.tag.o{background:var(--orange-light)}
.tag.b{background:var(--blue)}
.tag.l{background:#3a86d0}
.panel{position:absolute;left:0;bottom:0;width:420px;height:170px;color:#fff;padding:36px 0 0 90px;font-size:12px;line-height:1.6}
.panel.orange{background:var(--orange)}
.panel.blue{background:var(--blue);border-top-left-radius:14px;left:auto;right:0;width:410px;padding-left:70px}
.panel h3{font-size:14px;font-weight:700;margin-bottom:4px;padding-left:90px}
.panel .row svg{width:10px;height:10px}
.inside-right .ghost-mark{font-size:130px;left:60px;top:120px}
.inside-right .ghost-sub{position:absolute;left:70px;top:255px;font-family:'PT Serif',serif;font-size:20px;color:var(--ghost)}
</style>
</head>
<body>

<section class="spread outside">
  <article class="page back">
    <div class="top-bars"><span class="bar orange" style="left:0;width:250px"></span><span class="bar blue" style="left:260px;width:160px"></span></div>
    <div class="ghost-mark">KPW</div>
    <div class="brand"><span>KPW</span><span class="dot"></span></div>
    <div class="hours">
      <div class="label">Hours of <b>Operation</b></div>
      <div class="days">MONDAY - FRIDAY</div>
      <div class="time">8AM - 5PM CST</div>
    </div>
    <div class="divider"></div>
    <div class="contact-mini">
      <h4>Contact <span>Us :</span></h4>
      <div class="co">Keyline <span>Practice Works</span></div>
      <div class="row"><svg viewBox="0 0 10 10"><path d="M5 0a3.5 3.5 0 0 0-3.5 3.5C1.5 6 5 10 5 10s3.5-4 3.5-6.5A3.5 3.5 0 0 0 5 0z" fill="#e8590f"/></svg>218 Harlow Avenue Redfield, MN 55190</div>
      <div class="row"><svg viewBox="0 0 10 10"><path d="M2 0l2 2.5-1 1.2a6 6 0 0 0 3.3 3.3L7.5 6 10 8l-1.5 2C4 10 0 6 0 1.5z" fill="#e8590f"/></svg>800-555-0142 (Toll Free)</div>
      <div class="row"><svg viewBox="0 0 10 10"><path d="M2 0l2 2.5-1 1.2a6 6 0 0 0 3.3 3.3L7.5 6 10 8l-1.5 2C4 10 0 6 0 1.5z" fill="#e8590f"/></svg>651-555-0176</div>
      <div class="row"><svg viewBox="0 0 10 10"><rect x="1" y="4" width="8" height="4" fill="#e8590f"/><rect x="2.5" y="1" width="5" height="3" fill="#e8590f"/></svg>651-555-0193</div>
      <div class="row"><svg viewBox="0 0 10 10"><circle cx="5" cy="5" r="4" fill="none" stroke="#e8590f"/><path d="M1 5h8M5 1v8" stroke="#e8590f"/></svg>www.kpwclaims.com</div>
    </div>
    <svg class="bottom-band" viewBox="0 0 420 34"><path d="M0 18h300l20-10h100v26H0z" fill="#0b57a4"/><path d="M300 18l20-10h100v-4H312z" fill="#e8590f"/></svg>
  </article>

  <article class="page front">
    <svg class="hero" width="420" height="330" viewBox="0 0 420 330">
      <defs><radialGradient id="photoTone" cx="50%" cy="45%" r="60%"><stop offset="0" stop-color="#f3e6e0"/><stop offset=".6" stop-color="#c9dbe8"/><stop offset="1" stop-color="#8fb4d6"/></radialGradient></defs>
      <path d="M0 0h420v250C330 310 200 320 70 250 40 235 15 225 0 225z" fill="#0b57a4"/>
      <path d="M70 250c130 80 260 70 350 6v14C330 330 190 330 60 262z" fill="#e8590f"/>
      <circle cx="280" cy="130" r="150" fill="none" stroke="#2f7ac4" stroke-width="8"/>
      <circle cx="280" cy="130" r="142" fill="url(#photoTone)" role="img" aria-label="Photo of a smiling patient during a dental check-up"/>
    </svg>
    <div class="brand"><span>KPW</span><span class="dot"></span></div>
    <div class="welcome">
      <div class="small">Welcome To</div>
      <div class="big">Keyline Practice<br>Works</div>
    </div>
    <div class="web-pill"><svg width="9" height="9" viewBox="0 0 10 10"><circle cx="5" cy="5" r="4" fill="none" stroke="#fff"/><path d="M1 5h8M5 1v8" stroke="#fff"/></svg>www.kpwclaims.com</div>
  </article>
</section>

<section class="spread inside">
  <article class="page inside-left">
    <div class="top-bars"><span class="bar blue" style="left:0;width:140px"></span><span class="bar orange" style="left:150px;width:270px"></span></div>
    <div class="brand"><span>KPW</span><span class="dot"></span></div>
    <div class="intro">
      <div class="small">Welcome To</div>
      <h2>Keyline Practice Works</h2>
      <p>KPW is one of the largest electronic dental clearinghouses for dental claims and a leader in providing dental EDI solutions. We focus on bringing together Payers, Providers and Vendors to promote EDI transactions. Thousands of Dentists have chosen KPW as their electronic dental claims vendor of choice. Using our technology, KPW allows you to submit dental claims in seconds, the submission of Real Time Claim Statuses, Real Time Eligibility and getting Electronic Remittance Advice's (ERA's).</p>
      <p>KPW allows you to take your Electronic Remittance Advice (ERA) and post it directly into your Practice Management Software.</p>
      <p>Using Internet technology, KPW allows you to submit dental claims in minutes, access claim status in real time, and even submit all claims to all payers with a single click of the mouse. KPW also helps you connect directly to your payers, making it possible to cut weeks off your payment cycle.</p>
    </div>
    <div class="services-title">SERVICES</div>
    <div class="services">
      <div class="group-head">ELECTRONIC CLAIMS</div>
      <div class="tags">
        <span class="tag o">Real Time Eligibility</span><span class="tag o">Real Time Claim Status</span><span class="tag o">Remittances - EOB</span><span class="tag o">ERA/EOB AutoPost</span>
        <span class="tag o">Payment Manager</span><span class="tag o">Online Bill Pay</span><span class="tag o">Statements</span><span class="tag o">Accounts Receivable Aging</span>
      </div>
      <div class="group-head orange">PAYER LISTS</div>
      <div class="tags">
        <span class="tag b">Claims</span><span class="tag l">Real Time Eligibility</span><span class="tag b">Real Time Claim Status</span><span class="tag l">Electronic Remittances</span>
      </div>
    </div>
    <div class="panel orange">
      <h3>Contact Us :</h3>
      <div class="row"><svg viewBox="0 0 10 10"><path d="M5 0a3.5 3.5 0 0 0-3.5 3.5C1.5 6 5 10 5 10s3.5-4 3.5-6.5A3.5 3.5 0 0 0 5 0z" fill="#fff"/></svg>218 Harlow Avenue Redfield, MN 55190</div>
      <div class="row" style="padding-left:50px"><svg viewBox="0 0 10 10"><path d="M2 0l2 2.5-1 1.2a6 6 0 0 0 3.3 3.3L7.5 6 10 8l-1.5 2C4 10 0 6 0 1.5z" fill="#fff"/></svg>800-555-0142 (Toll Free)</div>
      <div class="row" style="padding-left:80px"><svg viewBox="0 0 10 10"><path d="M2 0l2 2.5-1 1.2a6 6 0 0 0 3.3 3.3L7.5 6 10 8l-1.5 2C4 10 0 6 0 1.5z" fill="#fff"/></svg>651-555-0176</div>
      <div class="row" style="padding-left:80px"><svg viewBox="0 0 10 10"><rect x="1" y="4" width="8" height="4" fill="#fff"/><rect x="2.5" y="1" width="5" height="3" fill="#fff"/></svg>651-555-0193</div>
      <div class="row" style="padding-left:70px"><svg viewBox="0 0 10 10"><circle cx="5" cy="5" r="4" fill="none" stroke="#fff"/><path d="M1 5h8M5 1v8" stroke="#fff"/></svg>www.kpwclaims.com</div>
    </div>
  </article>

  <article class="page inside-right">
    <div class="top-bars"><span class="bar orange" style="left:0;width:150px"></span><span class="bar blue" style="left:160px;width:260px"></span></div>
    <div class="ghost-mark">KPW</div>
    <div class="ghost-sub">Keyline Practice Works</div>
    <div class="panel blue">
      <h3>Contact Us :</h3>
      <div class="row"><svg viewBox="0 0 10 10"><path d="M5 0a3.5 3.5 0 0 0-3.5 3.5C1.5 6 5 10 5 10s3.5-4 3.5-6.5A3.5 3.5 0 0 0 5 0z" fill="#fff"/></svg>218 Harlow Avenue Redfield, MN 55190</div>
      <div class="row" style="padding-left:50px"><svg viewBox="0 0 10 10"><path d="M2 0l2 2.5-1 1.2a6 6 0 0 0 3.3 3.3L7.5 6 10 8l-1.5 2C4 10 0 6 0 1.5z" fill="#fff"/></svg>800-555-0142 (Toll Free)</div>
      <div class="row" style="padding-left:80px"><svg viewBox="0 0 10 10"><path d="M2 0l2 2.5-1 1.2a6 6 0 0 0 3.3 3.3L7.5 6 10 8l-1.5 2C4 10 0 6 0 1.5z" fill="#fff"/></svg>651-555-0176</div>
      <div class="row" style="padding-left:80px"><svg viewBox="0 0 10 10"><rect x="1" y="4" width="8" height="4" fill="#fff"/><rect x="2.5" y="1" width="5" height="3" fill="#fff"/></svg>651-555-0193</div>
      <div class="row" style="padding-left:70px"><svg viewBox="0 0 10 10"><circle cx="5" cy="5" r="4" fill="none" stroke="#fff"/><path d="M1 5h8M5 1v8" stroke="#fff"/></svg>www.kpwclaims.com</div>
    </div>
  </article>
</section>

</body>
</html>
```